VELMAR WEBSITE

need to create a new website for VELMAR ltd
the company deals with all aspects of safety products & safety wear
we need a simple website to show
ideas can be taken from following website whose products we shall distribute in kenya
www.qtw.co.uk
www.brovik.eu
www.tormanhardgear.com
www.qalvenworks.co.za

we need following tabs
1) home - basic company information
2) products - broken down to following categories ie gloves, head protection, ear protection, mouth protection, foot protection
3) contacts

the company profile is a reputable company dealing with all aspects of safety, HSE (health and safety equipment), and PPE (personal protective equipment)

the website should have the brovik logo for which we are an authorized distributor.
the brovi industrial range writeup can be picked from their website

Dear Designers, i shall be able to choose a final design in 2 weeks, sorry i have not been able to finalise this due to a personal reason

Target Market(s)

the buyers are all types of industry who care for their employees safety

Industry/Entity Type

Industrial

Requirements
Must have
• clean look, fresh look, user freindly
Nice to have
• clear images, quick links etc

```html
<!DOCTYPE html>
<html lang="en">
<head>
<meta charset="utf-8">
<title>VELMAR – Specialized Protective &amp; Industrial Products</title>
<link href="https://fonts.googleapis.com/css2?family=Open+Sans:wght@300;400;600;700&display=swap" rel="stylesheet">
<style>
:root{
  --navy:#14303f;
  --navy-dark:#0f2531;
  --yellow:#f2b705;
  --grey-text:#666a6e;
  --nav-text:#a7abaf;
  --band:#e6e9ef;
  --footer:#2b2e31;
  --footer-light:#34373a;
  --footer-bottom:#232527;
  --footer-text:#c9cbcd;
  --line:#d9dcdf;
  --social:#2f8fd6;
}
*{box-sizing:border-box;margin:0;padding:0}
html,body{width:960px;height:1200px;overflow:hidden}
body{position:relative;font-family:"Open Sans",Arial,sans-serif;background:#fff;color:var(--grey-text)}
.abs{position:absolute}

/* top bar */
.topbar{left:0;top:0;width:960px;height:35px;background:var(--navy)}
.topbar .item{top:0;height:35px;display:flex;align-items:center;gap:8px;color:#d7dde1;font-size:11.5px;border-left:1px solid #2a4756;padding:0 16px}
.topbar .phone{left:88px;width:126px}
.topbar .contact{left:214px;width:91px;border-right:1px solid #2a4756}
.topbar .social{left:320px;top:13px;display:flex;gap:5px}
.topbar .social span{width:8px;height:8px;background:#5d7380;border-radius:1px}
.search{left:616px;top:0;width:240px;height:35px;background:#3b3f43}
.search svg{position:absolute;left:11px;top:11px}

/* header */
.header{left:0;top:35px;width:960px;height:115px;background:#fff}
.logo{left:88px;top:62px;display:flex;align-items:center;gap:10px}
.logo .mark{width:26px;height:26px;background:var(--yellow)}
.logo .name{font-size:34px;font-weight:700;color:var(--navy);letter-spacing:1px}
.nav{left:415px;top:35px;display:flex;height:115px}
.nav a{width:91.5px;height:115px;display:flex;align-items:center;justify-content:center;font-size:13.5px;color:var(--nav-text);text-decoration:none;border-right:1px solid #eceef0;font-weight:300}
.nav a.active{background:var(--yellow);color:#fff;font-weight:400}

/* hero */
.hero{left:0;top:150px;width:960px;height:362px;background:linear-gradient(100deg,#8a97a3 0%,#a9b8c4 35%,#c9d6de 55%,#b89a5a 72%,#d9b420 80%,#c44b3a 92%,#b94436 100%)}
.hero-caption{left:86px;top:262px;width:366px;height:160px;background:rgba(40,42,44,.85);border-left:4px solid var(--yellow);padding:12px 20px}
.hero-caption h1{font-size:23.5px;font-weight:300;color:#fff;line-height:27px}
.hero-caption h1 .y{color:var(--yellow);font-weight:400}
.hero-caption h1 .yb{color:var(--yellow);font-weight:600}
.hero-caption p{margin-top:9px;font-size:12px;line-height:14.5px;color:#eee}
.hero-caption a{display:inline-block;margin-top:10px;font-size:12px;color:#fff}

/* categories */
.band{left:0;top:512px;width:960px;height:196px;background:var(--band)}
.panel{left:88px;top:494px;width:784px;height:214px;background:#fff}
.card{top:510px;width:176px}
.card .photo{width:176px;height:91px}
.card h3{height:37px;padding:13px 3px 0;font-size:14.5px;font-weight:400;color:#55595d;border-bottom:1px solid var(--line)}
.card p{padding:13px 4px 8px;font-size:11px;line-height:16px;font-weight:300;color:#55595d}
.card.active h3{background:var(--navy);color:#fff;border-bottom:none;font-weight:600}
.card.active p{background:var(--yellow);color:#fff;height:54px}

/* welcome */
.section-title{font-size:19px;font-weight:300;color:#4a4e52;display:flex;align-items:center;gap:12px}
.section-title::after{content:"";flex:1;border-top:3px double #dfe1e3}
.section-title .y{color:var(--yellow)}
.welcome{left:105px;top:734px;width:560px}
.welcome p{margin-top:11px;font-size:10.5px;line-height:14.6px;color:#7c8084}
.welcome p+p{margin-top:14px}
.btn{background:var(--navy);color:#fff;font-size:11px;border:none;height:24px;display:flex;align-items:center;justify-content:center}
.welcome .btn{position:absolute;left:-1px;top:154px;width:71px}
.quote{left:681px;top:734px;width:179px}
.quote .field{margin-top:7px;height:22px;border:1px solid #e3e5e7;border-radius:2px;font-size:8px;color:#8a8d90;padding:6px 9px;box-shadow:inset 0 1px 2px #eee}
.quote .field.first{margin-top:12px}
.quote .field.area{height:51px}
.quote .btn{position:absolute;right:0;top:154px;width:71px}

/* footer */
.footer{left:0;top:940px;width:960px;height:216px;background:var(--footer);overflow:hidden}
.footer .diag{position:absolute;left:0;top:0}
.fcol{top:978px}
.fcol h4{font-size:12.5px;font-weight:400;color:#e4e6e7;display:flex;align-items:center;gap:4px}
.fcol h4::after{content:"";flex:1;border-top:3px double #4b4f53}
.fcol ul{list-style:none;margin-top:17px}
.fcol li{font-size:9.5px;line-height:16px;color:var(--footer-text);text-decoration:underline}
.fcol p{margin-top:16px;font-size:9.5px;line-height:17.6px;color:var(--footer-text)}
.social-row{display:flex;gap:11px;margin-top:19px}
.social-row span{width:26px;height:26px;border-radius:3px;background:var(--social)}
.news h4{margin-top:20px}
.newsletter{margin-top:12px;width:213px;height:27px;background:#fff;border-radius:2px;display:flex;align-items:center;justify-content:space-between;padding:0 2px 0 10px}
.newsletter em{font-size:9px;color:#55595d}
.newsletter span{background:var(--yellow);color:#222;font-size:10.5px;height:23px;width:66px;display:flex;align-items:center;justify-content:center}
.bottombar{left:0;top:1156px;width:960px;height:44px;background:var(--footer-bottom);border-top:1px solid #3a3d40;display:flex;align-items:center;justify-content:space-between;padding:0 104px 0 90px;font-size:10.5px;color:#b9bcbf}
.bottombar nav{display:flex;gap:13px}
</style>
</head>
<body>

<div class="abs topbar">
  <div class="abs item phone">
    <svg width="12" height="12" viewBox="0 0 24 24"><path fill="#d7dde1" d="M6.6 10.8a15 15 0 0 0 6.6 6.6l2.2-2.2a1 1 0 0 1 1-.25 11.4 11.4 0 0 0 3.6.57 1 1 0 0 1 1 1V20a1 1 0 0 1-1 1A17 17 0 0 1 3 4a1 1 0 0 1 1-1h3.5a1 1 0 0 1 1 1c0 1.25.2 2.45.57 3.57a1 1 0 0 1-.25 1z"/></svg>
    0800-555-0192
  </div>
  <div class="abs item contact">
    <svg width="13" height="10" viewBox="0 0 26 20"><rect x="1" y="1" width="24" height="18" fill="none" stroke="#d7dde1" stroke-width="2"/><path d="M1 1l12 10L25 1" fill="none" stroke="#d7dde1" stroke-width="2"/></svg>
    Contact
  </div>
  <div class="abs social" aria-label="Social links"><span></span><span></span><span></span></div>
  <div class="abs search">
    <svg width="12" height="12" viewBox="0 0 24 24"><circle cx="10" cy="10" r="7" fill="none" stroke="#e5e7e9" stroke-width="3"/><path d="M15 15l7 7" stroke="#e5e7e9" stroke-width="3"/></svg>
  </div>
</div>

<div class="abs header"></div>
<div class="abs logo"><span class="mark"></span><span class="name">VELMAR</span></div>
<nav class="abs nav">
  <a class="active">HOME</a><a>PRODUCTS</a><a>ABOUT US</a><a>AGENCIES</a><a>CONTACT US</a>
</nav>

<div class="abs hero" role="img" aria-label="Construction site with cranes and a worker in a safety vest holding a yellow hard hat and work gloves"></div>
<div class="abs hero-caption">
  <h1><span class="y">VELMAR</span> Specialized Protective<br><span class="yb">&amp;</span> Industrial <span class="yb">Products</span></h1>
  <p>Lorem ipsum dolor sit amet, consectetur adipisicing elit, sed do eiusmod tempor incididunt ut labore et dolore magna aliqua...</p>
  <a>READ MORE</a>
</div>

<div class="abs band"></div>
<div class="abs panel"></div>

<div class="abs card" style="left:104px">
  <div class="photo" role="img" aria-label="Worker wearing a blue hard hat and safety glasses" style="background:linear-gradient(135deg,#9bb0c4,#5b7fa8 45%,#c9cdd2)"></div>
  <h3>HEAD PROTECTION</h3>
  <p>Lorem ipsum dolor sit amet Cons-ectetur adipsicing elit.</p>
</div>
<div class="abs card active" style="left:296px">
  <div class="photo" role="img" aria-label="Hands pulling on blue protective gloves" style="background:linear-gradient(135deg,#3f6670,#5d5a4c 55%,#3d5e68)"></div>
  <h3>HAND PROTECTION</h3>
  <p>Lorem ipsum dolor sit amet Con-sectetur adipsicing elit.</p>
</div>
<div class="abs card" style="left:489px">
  <div class="photo" role="img" aria-label="Pair of worn leather work boots" style="background:linear-gradient(180deg,#f1b04a,#d98b3a 50%,#7a4a32)"></div>
  <h3>FOOT PROTECTION</h3>
  <p>Lorem ipsum dolor sit amet Cons-ectetur adipsicing elit.</p>
</div>
<div class="abs card" style="left:681px">
  <div class="photo" role="img" aria-label="Two clear mouth guards on a wooden surface" style="background:linear-gradient(135deg,#7a4e26,#a8753f 50%,#6c4220)"></div>
  <h3>MOUTH PROTECTION</h3>
  <p>Lorem ipsum dolor sit amet Cons-ectetur adipsicing elit.</p>
</div>

<section class="abs welcome">
  <h2 class="section-title"><span>Welcome To <span class="y">VELMAR</span> Specialized</span></h2>
  <p>Lorem ipsum dolor sit amet, consectetur adipisicing elit, sed do eiusmod tempor incididunt ut labore et dolore magna aliqua. Ut enim ad minim veniam, quis nostrud exercitation ullamco laboris nisi ut aliquip ex ea commodo consequat. Duis reprehenderit in voluptate velit esse cillum dolore eu fugiat nulla pariatur. Excepteur sint occaecat cupidatat non proident, sunt in culpa qui officia deserunt mollit anim id est laborum.</p>
  <p>Lorem ipsum dolor sit amet, consectetur adipisicing elit, sed do eiusmod tempor incididunt ut labore et dolore magna aliqua quis nostrud exercitation ullamco laboris nisi ut aliquip ex ea commodo consequat.</p>
  <div class="btn">Read More</div>
</section>

<section class="abs quote">
  <h2 class="section-title"><span>Get A Quote</span></h2>
  <div class="field first">Enter your name...</div>
  <div class="field">Enter your email...</div>
  <div class="field area">Enter your comment...</div>
  <div class="btn">Submit</div>
</section>

<footer class="abs footer">
  <svg class="diag" width="960" height="216" viewBox="0 0 960 216"><path d="M360 216L960 0V216Z" fill="#34373a"/></svg>
</footer>

<div class="abs fcol" style="left:89px;width:124px">
  <h4>Contact Info</h4>
  <ul>
    <li>lorem ipsum</li><li>dolor sit amet 106</li><li>1404 consecteture</li><li>adipiscing elit</li><li>eMail: info@Velmar.com</li><li>Phone: +800-555-0192</li>
  </ul>
</div>
<div class="abs fcol" style="left:253px;width:169px">
  <h4>About Us</h4>
  <p>Lorem ipsum dolor sit amet, consectetur adipisicing elit, sed do eiusmod tempor incididunt ut labore et dolore magna aliqua. Ut enim ad minim veniam.</p>
</div>
<div class="abs fcol" style="left:461px;width:124px">
  <h4>Company Info</h4>
  <ul><li>Lorem ipsum</li><li>dolor sit amet</li><li>consectetur</li><li>adipsicing elit</li></ul>
</div>
<div class="abs fcol" style="left:625px;width:213px">
  <h4>Stay updates on our Socail Network</h4>
  <div class="social-row" aria-label="Social network links"><span></span><span></span><span></span></div>
  <div class="news"><h4>Join Our Newsletter</h4></div>
  <div class="newsletter"><em>Enter your email address</em><span>Subscribe</span></div>
</div>

<div class="abs bottombar">
  <nav><span>Home</span><span>About Us</span><span>Our Products</span><span>Agencies</span><span>Contact Us</span></nav>
  <span>© Copyrights 2013 All rights Reserved</span>
</div>

</body>
</html>
```